Clean invitation for a wedding

Design a wedding invitation.
Those examples in attachment. They are looking for this style, about the same construction. Back with the symbols etc.

Clean sleek design.

marriage name:
Kemp & Rosetta
02.06.23

You can copy the rest of the texts from the examples.

```html
<!DOCTYPE html>
<html lang="en">
<head>
<meta charset="UTF-8">
<title>Kemp &amp; Rosetta – Wedding Invitation</title>
<link rel="stylesheet" href="https://fonts.googleapis.com/css2?family=Mrs+Saint+Delafield&family=Montserrat:wght@500;600&family=Bodoni+Moda:wght@500&display=swap">
<style>
  :root {
    --page: #ffffff;
    --card: #ebebe4;
    --ink: #1d1d1b;
    --icon-fill: #d9d9d1;
  }
  * { margin: 0; padding: 0; box-sizing: border-box; }
  html, body { width: 1200px; height: 1200px; overflow: hidden; background: var(--page); }
  .canvas { position: relative; width: 1200px; height: 1200px; }
  .card {
    position: absolute; top: 225px; width: 536px; height: 750px;
    background: var(--card); color: var(--ink);
  }
  .card--invite { left: 46px; }
  .card--program { left: 618px; }
  .caps {
    position: absolute; left: 0; width: 100%; text-align: center;
    font-family: "Montserrat", sans-serif; font-weight: 600;
    font-size: 11.5px; letter-spacing: 0.22em; line-height: 1.25; text-transform: uppercase;
  }
  .script { font-family: "Mrs Saint Delafield", cursive; font-weight: 400; line-height: 1; position: absolute; }
  .intro { top: 74px; }
  .name-first { left: 150px; top: 120px; font-size: 118px; }
  .name-second { left: 168px; top: 228px; font-size: 118px; white-space: nowrap; }
  .date {
    position: absolute; left: 0; width: 100%; top: 414px; text-align: center;
    font-family: "Bodoni Moda", serif; font-weight: 500; font-size: 46px; letter-spacing: 0.16em;
  }
  .time-line { top: 468px; }
  .venue { top: 513px; }
  .rsvp-title { left: 0; width: 100%; text-align: center; top: 580px; font-size: 52px; }
  .rsvp-note { top: 648px; }

  .program-title { left: 0; width: 100%; text-align: center; top: 40px; font-size: 120px; padding-left: 10px; }
  .icon-column { position: absolute; left: 134px; top: 196px; width: 86px; height: 486px; }
  .timeline { position: absolute; left: 0; top: 0; width: 536px; height: 750px; }
  .event { position: absolute; left: 246px; width: 200px; }
  .event .caps { position: absolute; left: 0; width: 100%; font-size: 11px; }
</style>
</head>
<body>
<div class="canvas">
  <section class="card card--invite">
    <p class="caps intro">Please join us to<br>celebrate the wedding of</p>
    <h1 class="script name-first">Kemp</h1>
    <p class="script name-second">&amp; Rosetta</p>
    <p class="date">02.06.23</p>
    <p class="caps time-line">10' clock in the afternoon</p>
    <p class="caps venue">At Harbor Pine Gardens<br>Malibu, California</p>
    <p class="script rsvp-title">RSVP</p>
    <p class="caps rsvp-note">Kindly RSVP to Kemp by February 6th 2023<br>kemprosettawedding@yourmail.com</p>
  </section>

  <section class="card card--program">
    <h2 class="script program-title">Program</h2>
    <svg class="icon-column" viewBox="0 0 86 486" role="img" aria-label="Column of line icons: wedding rings, champagne toast, wedding cake, dinner plate, dancing couple, music notes">
      <rect width="86" height="486" rx="6" fill="var(--icon-fill)"/>
    </svg>
    <svg class="timeline" viewBox="0 0 536 750" aria-hidden="true">
      <line x1="268" y1="228" x2="268" y2="642" stroke="var(--ink)" stroke-width="2.5"/>
      <g fill="var(--ink)">
        <circle cx="268" cy="228" r="3.5"/>
        <circle cx="268" cy="313" r="3.5"/>
        <circle cx="268" cy="398" r="3.5"/>
        <circle cx="268" cy="483" r="3.5"/>
        <circle cx="268" cy="568" r="3.5"/>
        <circle cx="276" cy="646" r="3.5"/>
      </g>
    </svg>
    <div class="event" style="top:211px"><p class="caps" style="top:0">13:30</p><p class="caps" style="top:30px">Vielse</p></div>
    <div class="event" style="top:301px"><p class="caps" style="top:0">15:00</p><p class="caps" style="top:29px">Forfrisgning<br>og hygge</p></div>
    <div class="event" style="top:390px"><p class="caps" style="top:0">16:00</p><p class="caps" style="top:29px">Bryllupscage</p></div>
    <div class="event" style="top:464px"><p class="caps" style="top:0">17:30</p><p class="caps" style="top:30px">Middag</p></div>
    <div class="event" style="top:554px"><p class="caps" style="top:0">23:00</p><p class="caps" style="top:29px">Lorerm ipsum</p></div>
  </section>
</div>
</body>
</html>
```